Young Makers Competition Event For Teenagers Needs Promo Graphics

I am in need of graphics for 2019 Northmere Young Makers Festival. It is a Young Makers competition event for teenagers. I need graphics to make an 11x17 poster and a main title graphic that I can use for digital (social, 16x9 for screens, etc). Graphic should include the following 2 logos: the QW Brightpath logo (this is who we are) and the "circles" logo is the logo of Young Makers Festival so that can be incorporated but is not mandatory and does not need to be in color. Tag line for Young Makers is "Discover. Develop. Deploy." Again, this is optional. Looking for an artistic design - geometric shapes, bright colors, or something along those lines. Something that speaks to teenagers and especially creatives/Young Makers types. Additionally, Post should include:
Maple Ridge Chapel
March 29-30
(registration & cost info may be added to the poster before design is finalized; still working on those details)

```html
<!DOCTYPE html>
<html lang="en">
<head>
<meta charset="utf-8">
<title>Northmere Young Makers Festival</title>
<link rel="stylesheet" href="https://fonts.googleapis.com/css2?family=Bebas+Neue&family=Montserrat:wght@600;700&display=swap">
<style>
  :root {
    --paper: #fbf7e8;
    --navy: #273b8c;
    --cyan: #33c3f0;
    --red: #e84326;
    --pink: #e0405a;
    --yellow: #f7b21a;
    --teal: #8fd0d8;
    --orange: #e8582a;
    --web: #2aa6a8;
  }
  html, body { margin: 0; padding: 0; overflow: hidden; background: var(--paper); }
  .poster { display: block; width: 873px; height: 1200px; }
  .bg { fill: var(--paper); }
  .navy { fill: var(--navy); }
  .cyan { fill: var(--cyan); }
  .red { fill: var(--red); }
  .pink { fill: var(--pink); }
  .yellow { fill: var(--yellow); }
  .teal { fill: var(--teal); }
  .orange { fill: var(--orange); }
  .bar-cyan { stroke: var(--cyan); stroke-width: 15; stroke-linecap: butt; }
  .bar-navy { stroke: var(--navy); stroke-width: 12; }
  .bar-pink { stroke: var(--pink); stroke-width: 10; }
  .frame-outer { fill: none; stroke: var(--yellow); stroke-width: 1.3; }
  .frame-inner { fill: none; stroke: var(--cyan); stroke-width: 2; }
  .rings { fill: none; stroke: var(--orange); stroke-width: 0.9; }
  .rule { stroke: var(--navy); stroke-width: 3; }
  .stripes { stroke: var(--pink); stroke-width: 3; }
  .kicker { font-family: "Bebas Neue", sans-serif; font-size: 44px; fill: var(--cyan); letter-spacing: 1px; }
  .title { font-family: "Bebas Neue", sans-serif; font-size: 96px; fill: var(--navy); }
  .brand { font-family: "Montserrat", sans-serif; font-weight: 700; font-size: 20px; fill: var(--cyan); }
  .festival-mark { font-family: "Montserrat", sans-serif; font-weight: 700; font-size: 8.5px; fill: var(--navy); letter-spacing: 1px; }
  .date { font-family: "Montserrat", sans-serif; font-weight: 700; font-size: 30px; fill: var(--pink); }
  .venue { font-family: "Montserrat", sans-serif; font-weight: 600; font-size: 19px; fill: var(--pink); letter-spacing: 0.5px; }
  .web { font-family: "Montserrat", sans-serif; font-weight: 600; font-size: 10.5px; fill: var(--web); }
</style>
</head>
<body>
<svg class="poster" viewBox="0 0 576 792" xmlns="http://www.w3.org/2000/svg" role="img" aria-label="Northmere Young Makers Festival poster">
  <rect class="bg" width="576" height="792"/>

  <!-- top decoration -->
  <line class="bar-navy" x1="-6" y1="40" x2="70" y2="-6"/>
  <line class="bar-navy" x1="-6" y1="70" x2="100" y2="6"/>
  <polygon class="teal" points="576,0 576,128 462,0"/>
  <circle class="yellow" cx="0" cy="300" r="44"/>
  <rect class="red" x="40" y="120" width="46" height="46" transform="rotate(45 63 143)"/>
  <g class="teal">
    <circle cx="130" cy="34" r="2"/><circle cx="140" cy="34" r="2"/><circle cx="150" cy="34" r="2"/><circle cx="160" cy="34" r="2"/>
    <circle cx="130" cy="44" r="2"/><circle cx="140" cy="44" r="2"/><circle cx="150" cy="44" r="2"/><circle cx="160" cy="44" r="2"/>
    <circle cx="130" cy="54" r="2"/><circle cx="140" cy="54" r="2"/><circle cx="150" cy="54" r="2"/><circle cx="160" cy="54" r="2"/>
  </g>
  <polygon class="orange" points="388,64 424,64 406,36"/>
  <line class="bar-cyan" x1="150" y1="110" x2="196" y2="70"/>
  <rect class="pink" x="440" y="96" width="14" height="14" transform="rotate(45 447 103)"/>
  <line class="bar-cyan" x1="470" y1="230" x2="530" y2="170"/>
  <line class="bar-cyan" x1="492" y1="246" x2="540" y2="198"/>
  <g class="orange">
    <polygon points="20,210 34,210 27,218"/><polygon points="20,220 34,220 27,228"/>
    <polygon points="20,230 34,230 27,238"/>
  </g>
  <rect class="cyan" x="100" y="200" width="12" height="12" transform="rotate(45 106 206)"/>
  <circle class="teal" cx="546" cy="286" r="13"/>

  <!-- middle sides -->
  <g class="stripes">
    <line x1="534" y1="370" x2="570" y2="370"/><line x1="534" y1="379" x2="570" y2="379"/>
    <line x1="534" y1="388" x2="570" y2="388"/><line x1="534" y1="397" x2="570" y2="397"/>
    <line x1="534" y1="406" x2="570" y2="406"/><line x1="534" y1="415" x2="570" y2="415"/>
  </g>
  <polygon class="orange" points="18,440 62,440 40,404"/>
  <rect class="yellow" x="82" y="392" width="11" height="11" transform="rotate(45 87 397)"/>
  <rect class="navy" x="490" y="460" width="14" height="14" transform="rotate(45 497 467)"/>
  <rect class="red" x="528" y="470" width="58" height="58" transform="rotate(45 557 499)"/>

  <!-- lower decoration -->
  <g class="rings">
    <circle cx="84" cy="530" r="6"/><circle cx="84" cy="530" r="12"/>
    <circle cx="84" cy="530" r="18"/><circle cx="84" cy="530" r="24"/>
  </g>
  <line class="bar-pink" x1="440" y1="560" x2="500" y2="600"/>
  <rect class="cyan" x="134" y="600" width="12" height="12" transform="rotate(45 140 606)"/>
  <line class="bar-cyan" x1="26" y1="640" x2="80" y2="600"/>
  <circle class="yellow" cx="0" cy="792" r="96"/>
  <line class="bar-navy" x1="120" y1="800" x2="190" y2="724"/>
  <g class="navy">
    <rect x="440" y="700" width="3" height="3"/><rect x="446" y="700" width="3" height="3"/><rect x="452" y="700" width="3" height="3"/><rect x="458" y="700" width="3" height="3"/>
    <rect x="440" y="706" width="3" height="3"/><rect x="446" y="706" width="3" height="3"/><rect x="452" y="706" width="3" height="3"/><rect x="458" y="706" width="3" height="3"/>
    <rect x="440" y="712" width="3" height="3"/><rect x="446" y="712" width="3" height="3"/><rect x="452" y="712" width="3" height="3"/><rect x="458" y="712" width="3" height="3"/>
  </g>
  <rect class="red" x="500" y="700" width="80" height="80" transform="rotate(45 540 740)"/>
  <polygon class="teal" points="400,792 470,792 435,748"/>
  <rect class="pink" x="520" y="640" width="14" height="14" transform="rotate(45 527 647)"/>

  <!-- central frame -->
  <polygon class="frame-outer" points="289,66 511,289 289,511 67,289"/>
  <polyline class="frame-inner" points="236,124 289,71 342,124"/>
  <polyline class="frame-inner" points="112,262 92,289 112,316"/>
  <polyline class="frame-inner" points="466,262 486,289 466,316"/>
  <polyline class="frame-inner" points="236,454 289,501 342,454"/>

  <!-- festival mark -->
  <rect class="navy" x="283" y="122" width="12" height="12"/>
  <text class="festival-mark" x="289" y="150" text-anchor="middle">YOUNG MAKERS</text>

  <!-- headline -->
  <text class="kicker" x="288" y="52" text-anchor="middle">NORTHMERE</text>
  <text class="title" x="289" y="262" text-anchor="middle" textLength="318" lengthAdjust="spacingAndGlyphs">YOUNG MAKERS</text>
  <text class="title" x="289" y="356" text-anchor="middle" textLength="290" lengthAdjust="spacingAndGlyphs">FESTIVAL</text>
  <text class="brand" x="289" y="408" text-anchor="middle">QW Brightpath</text>

  <!-- event details -->
  <line class="rule" x1="178" y1="568" x2="410" y2="568"/>
  <text class="date" x="294" y="605" text-anchor="middle">29-30 MART</text>
  <text class="venue" x="294" y="632" text-anchor="middle">Maple Ridge Chapel</text>
  <line class="rule" x1="178" y1="646" x2="410" y2="646"/>

  <!-- footer -->
  <circle class="navy" cx="266" cy="736" r="8"/>
  <circle class="navy" cx="290" cy="736" r="8"/>
  <circle class="navy" cx="314" cy="736" r="8"/>
  <text class="web" x="290" y="763" text-anchor="middle">www.northmeremakers.org</text>
</svg>
</body>
</html>
```